Cash For clothes textile recycling company leaflet design

We need flyer design for textile recycling company called RK BRIGHTFOLD LTD , we pay cash for peoples unwanted clothes and helping enviroment by moving used unwanted clothing to other countries in need, we are not charity company,as we pay money for people for their unwanted clothing. We would like to see designs that use yellow pink and bright green collors (more summer themes) you can use one or few logos we have uploaded

Industry/Entity Type

Textile

Font styles to use
Decorative

Colors
fbee3d
e34197
33a6d7
abd036
a54499
fece3e

Requirements
Nice to have
• you can play with logos, everything can be colourful, more soft colours, people shouldn't be pushed away from reading the leaflet, some sort of logos with smiles or so can appear as well
Should not have
• no big notes or cash pictures (can be something small) nothing dark or sad looking.

```html
<!DOCTYPE html>
<html lang="en">
<head>
<meta charset="utf-8">
<title>RK Brightfold Ltd – We Pay Cash For Your Unwanted Clothes</title>
<link href="https://fonts.googleapis.com/css2?family=PT+Sans:ital,wght@0,400;0,700;1,400;1,700&display=swap" rel="stylesheet">
<style>
  :root {
    --green: #abd036;
    --pink: #e34197;
    --purple: #a54499;
    --yellow: #fbee3d;
    --amber: #fece3e;
    --red: #e2342b;
    --cream: #fdfbe8;
    --ink: #3a3a3a;
    --white: #ffffff;
  }
  * { margin: 0; padding: 0; box-sizing: border-box; }
  html, body { width: 935px; height: 1200px; overflow: hidden; background: var(--white); }
  body { font-family: "PT Sans", Arial, sans-serif; color: var(--ink); }

  .flyer { position: relative; width: 935px; height: 1200px; background: var(--cream); overflow: hidden; }

  .masthead {
    position: absolute; left: 0; top: 0; width: 935px; height: 132px;
    background: var(--green); text-align: center; padding-top: 14px;
  }
  .masthead__lead { color: var(--pink); font-weight: 700; font-size: 44px; line-height: 1.05; letter-spacing: 0.5px; }
  .masthead__title { color: var(--white); font-weight: 700; font-size: 44px; line-height: 1.1; letter-spacing: 0.5px; }

  .hero {
    position: absolute; left: 0; top: 132px; width: 935px; height: 440px;
    background: linear-gradient(90deg, #c9b8a6 0%, #e7ddd2 35%, #f1eeea 55%, #d7d3cf 75%, #b9c2cc 100%);
  }
  .badge {
    position: absolute; left: 18px; top: 146px; width: 146px; height: 146px;
    border-radius: 50%; background: var(--white);
    display: flex; align-items: center; justify-content: center; text-align: center;
    color: var(--red); font-weight: 700; font-size: 22px; line-height: 1.1;
  }
  .wave { position: absolute; left: 0; top: 500px; width: 935px; height: 110px; }

  .story {
    position: absolute; left: 0; top: 560px; width: 355px; height: 508px;
    background: var(--green); padding: 16px 16px 0 14px;
    color: var(--white); font-style: italic; font-size: 15.5px; line-height: 1.28; text-align: justify;
  }
  .story p + p { margin-top: 0; }

  .offer { position: absolute; left: 384px; top: 618px; width: 520px; }
  .offer__rate { color: var(--purple); font-size: 22px; line-height: 1.3; }
  .offer__rate strong { font-weight: 700; }
  .offer__body { color: var(--ink); font-size: 20.5px; line-height: 1.3; }

  .rules {
    position: absolute; left: 384px; top: 834px; width: 508px; height: 218px;
    background: var(--amber); display: grid; grid-template-columns: 210px 1fr;
  }
  .rules__head {
    background: var(--yellow); color: var(--red); font-weight: 700; font-size: 15px;
    padding: 5px 12px; height: 28px;
  }
  .rules__list { list-style: none; padding: 6px 12px; font-size: 14.5px; line-height: 1.22; color: var(--ink); }
  .rules__list li::before { content: "• "; }
  .rules__list--accept { grid-column: 1; grid-row: 2; }
  .rules__list--reject { grid-column: 2; grid-row: 2; }

  .footer {
    position: absolute; left: 0; top: 1080px; width: 935px; height: 72px;
    background: var(--purple); display: flex; align-items: center; padding-left: 22px; color: var(--white);
  }
  .footer__name { font-weight: 700; font-size: 31px; letter-spacing: 0.3px; }
  .footer__reg { font-weight: 700; font-size: 14px; margin-left: 24px; margin-top: 6px; }
</style>
</head>
<body>
<main class="flyer">
  <header class="masthead">
    <p class="masthead__lead">WE PAY CASH</p>
    <h1 class="masthead__title">FOR YOUR UNVANTED CLOTHES</h1>
  </header>

  <div class="hero" role="img" aria-label="Photo of a smiling woman holding a box of folded clothes beside a rail of shirts on hangers"></div>
  <div class="badge">RK<br>Brightfold</div>

  <svg class="wave" viewBox="0 0 935 110" preserveAspectRatio="none" aria-hidden="true">
    <path d="M0 60 C250 -5 600 -10 935 30 L935 110 L0 110 Z" fill="var(--cream)"/>
    <path d="M0 38 C260 -25 620 -20 935 6 L935 36 C620 8 260 12 0 72 Z" fill="var(--pink)"/>
    <path d="M0 72 C260 12 620 8 935 36 L935 44 C620 16 260 20 0 80 Z" fill="var(--yellow)"/>
  </svg>

  <section class="story">
    <p>For some this industry appears exploitative, but we are incredibly proud of our business's work as textile recyclers. We are not oil companies doing deals with corrupt governments to buy a country's natural resources, nor are we selling old PCs to be dismantled by children breathing in toxic fume; this is a family business doing business with other family businesses to ensure that much-needed clothing can be bought by customers who want it. And we are helping to tackle the problem of what to do with the 900,000 tons of unwanted clothes, which in 2009 the Department of Forestry and Rural Affairs, said went into landfill each year. Things we do will not change the world, but at least it makes a difference.</p>
    <p>Thank you for reading this, and remember - small things make a big difference!</p>
  </section>

  <section class="offer">
    <p class="offer__rate">We will pay <strong>55p per kg</strong> just call <strong>07700900418</strong><br>or email <strong>brightfold4417@mailbox.co.uk</strong></p>
    <p class="offer__body">to arrange collection, and our helpful and friendly staff will make sure that your unwanted clothing will be collected as soon as possible, and pay you cash straight away!</p>
  </section>

  <section class="rules">
    <h2 class="rules__head">WE ACCEPT:</h2>
    <h2 class="rules__head">WE DO NOT ACCEPT:</h2>
    <ul class="rules__list rules__list--accept">
      <li>Any clean dry clothing</li>
      <li>Paired shoes</li>
      <li>Belts</li>
      <li>Handbags</li>
    </ul>
    <ul class="rules__list rules__list--reject">
      <li>Bad quality, wet, stained, mouldy or ripped items</li>
      <li>Used socks, underwear</li>
      <li>Quilts, duvets, pillows</li>
      <li>Bedding, curtains</li>
      <li>Carpets, mats, rugs</li>
      <li>Books</li>
      <li>CDs, DVDs, audio and video tapes</li>
      <li>Glass, metal, wood</li>
    </ul>
  </section>

  <footer class="footer">
    <span class="footer__name">RK BRIGHTFOLD LTD</span>
    <span class="footer__reg">REGISTERED IN ENGLAND &amp; WALES / COMPANY NUMBER: 08371246</span>
  </footer>
</main>
</body>
</html>
```